Clean, Fresh Business Card Design Needed

We need a business card design for a new business we have taken over called "Bonders and Fillers". We got a logo through this website which i have attached. We are wanting something that is vibrant but clean and fresh. Our business mainly sells glue. Maybe a cool design/slogan on the back? Modern, sleek.

Industry/Entity Type

Business

Contact Information for Business Card

Name: Ewan Tressider, Managing Director. Address: 164 Kelmond Road, Tauranga 3117, Phone: 07 462 3947 Mobile: 021 354 921 Fax: 07 462 5086 Email: bondfill.mail@pelorix.co.nz, Web: www.stickwarex.co.nz

Font styles to use
Serif

Requirements
Must have
• All business card details, logo.
Nice to have
• Design, slogan on back of card

```html
<!DOCTYPE html>
<html lang="en">
<head>
<meta charset="utf-8">
<title>Bonders and Fillers – Business Card</title>
<link rel="stylesheet" href="https://fonts.googleapis.com/css2?family=Libre+Baskerville:ital,wght@0,400;0,700;1,400&display=swap">
<style>
  :root {
    --navy: #2a3990;
    --royal: #3f57a8;
    --ink: #05060c;
    --paper: #ffffff;
    --mist: #e4e7f4;
    --haze: #c9d2f0;
    --stage: #eceae6;
  }
  * { box-sizing: border-box; margin: 0; padding: 0; }
  html, body { width: 1200px; height: 960px; overflow: hidden; }
  body {
    background: var(--stage);
    font-family: "Libre Baskerville", Georgia, serif;
    position: relative;
  }
  .card {
    position: absolute;
    width: 720px;
    height: 440px;
    left: 240px;
    box-shadow: 0 6px 18px rgba(0,0,0,.25);
  }
  /* Back of card */
  .card-back {
    top: 24px;
    background: radial-gradient(ellipse 55% 60% at 52% 48%, #4159a8 0%, #2f4396 40%, #151b3e 72%, var(--ink) 100%);
    display: flex;
    flex-direction: column;
    align-items: center;
    justify-content: center;
    color: var(--paper);
  }
  .back-mark {
    width: 130px; height: 130px;
    background: var(--paper);
    border-radius: 12px;
  }
  .back-name {
    margin-top: 24px;
    font-size: 44px;
    font-weight: 400;
    letter-spacing: 3px;
    text-transform: uppercase;
    text-align: center;
    line-height: 1.1;
  }
  .back-slogan {
    margin-top: 16px;
    font-size: 16px;
    font-style: italic;
    letter-spacing: 1px;
    color: var(--haze);
  }
  /* Front of card */
  .card-front {
    top: 496px;
    background: radial-gradient(ellipse 80% 80% at 45% 45%, var(--paper) 55%, var(--mist) 100%);
    color: var(--navy);
    padding: 60px 44px 0 44px;
  }
  .front-head {
    display: flex;
    justify-content: space-between;
    align-items: center;
  }
  .person { text-align: center; width: 320px; white-space: nowrap; }
  .person-name {
    font-weight: 700;
    font-size: 24px;
    letter-spacing: .3px;
    text-transform: uppercase;
  }
  .person-title {
    font-size: 17px;
    text-transform: uppercase;
    letter-spacing: .5px;
    margin-top: 4px;
  }
  .brand { display: flex; align-items: center; gap: 10px; }
  .brand-mark { width: 64px; height: 64px; background: var(--navy); border-radius: 4px; flex: none; }
  .brand-name {
    font-size: 21px;
    text-transform: uppercase;
    letter-spacing: 1.5px;
    line-height: 1.12;
    white-space: nowrap;
  }
  .contacts {
    display: grid;
    grid-template-columns: 420px 1fr;
    row-gap: 34px;
    margin-top: 80px;
    font-size: 17px;
    letter-spacing: .3px;
  }
  .contact { display: flex; align-items: center; gap: 12px; white-space: nowrap; }
  .contact svg { width: 22px; height: 22px; fill: var(--navy); flex: none; }
</style>
</head>
<body>

<section class="card card-back" aria-label="Card back">
  <div class="back-mark"></div>
  <div class="back-name">Bonders<br>and Fillers</div>
  <div class="back-slogan">Made to hold, built to last</div>
</section>

<section class="card card-front" aria-label="Card front">
  <header class="front-head">
    <div class="person">
      <div class="person-name">Ewan Tressider</div>
      <div class="person-title">Managing Director</div>
    </div>
    <div class="brand">
      <div class="brand-mark"></div>
      <div class="brand-name">Bonders<br>and Fillers</div>
    </div>
  </header>

  <div class="contacts">
    <div class="contact">
      <svg viewBox="0 0 24 24" aria-hidden="true"><path d="M12 1a8 8 0 0 0-8 8c0 6 8 14 8 14s8-8 8-14a8 8 0 0 0-8-8zm0 11a3 3 0 1 1 0-6 3 3 0 0 1 0 6z"/></svg>
      <span>164 Kelmond Road, Tauranga 3117</span>
    </div>
    <div class="contact">
      <svg viewBox="0 0 24 24" aria-hidden="true"><path d="M6.6 10.8a15 15 0 0 0 6.6 6.6l2.2-2.2a1 1 0 0 1 1-.25 11.4 11.4 0 0 0 3.6.57 1 1 0 0 1 1 1V20a1 1 0 0 1-1 1A17 17 0 0 1 3 4a1 1 0 0 1 1-1h3.5a1 1 0 0 1 1 1c0 1.25.2 2.450.57 3.6a1 1 0 0 1-.25 1z"/></svg>
      <span>07 462 3947</span>
    </div>
    <div class="contact">
      <svg viewBox="0 0 24 24" aria-hidden="true"><path d="M2 5h20v14H2zm2 2v.5l8 5 8-5V7zm0 3v7h16v-7l-8 5z"/></svg>
      <span>bondfill.mail@pelorix.co.nz</span>
    </div>
    <div class="contact">
      <svg viewBox="0 0 24 24" aria-hidden="true"><path d="M7 1h10a2 2 0 0 1 2 2v18a2 2 0 0 1-2 2H7a2 2 0 0 1-2-2V3a2 2 0 0 1 2-2zm0 3v14h10V4zm5 15.5a1 1 0 1 0 0 2 1 1 0 0 0 0-2z"/></svg>
      <span>021 354 921</span>
    </div>
    <div class="contact">
      <svg viewBox="0 0 24 24" aria-hidden="true"><path d="M12 2a10 10 0 1 0 0 20 10 10 0 0 0 0-20zm7.9 9h-3.4a15 15 0 0 0-1.3-6.3A8 8 0 0 1 19.9 11zM12 4.1c1 1.2 2.3 3.6 2.5 6.9h-5C9.7 7.7 11 5.3 12 4.1zM8.8 4.7A15 15 0 0 0 7.5 11H4.1a8 8 0 0 1 4.7-6.3zM4.1 13h3.4a15 15 0 0 0 1.3 6.3A8 8 0 0 1 4.1 13zm7.9 6.9c-1-1.2-2.3-3.6-2.5-6.9h5c-.2 3.3-1.5 5.7-2.5 6.9zm3.2-.6a15 15 0 0 0 1.3-6.3h3.4a8 8 0 0 1-4.7 6.3z"/></svg>
      <span>www.stickwarex.co.nz</span>
    </div>
    <div class="contact">
      <svg viewBox="0 0 24 24" aria-hidden="true"><path d="M6 2h10l2 2v4H6zM3 9h18a1 1 0 0 1 1 1v7h-4v5H6v-5H2v-7a1 1 0 0 1 1-1zm5 6v5h8v-5zm1 1h6v1H9zm0 2h6v1H9z"/></svg>
      <span>07 462 5086</span>
    </div>
  </div>
</section>

</body>
</html>
```